KVT Business Cards

We require business cards for our business. We would like a matte black back to the card, with our logo centred in the middle. The front side of the card is open to design.

Target Market(s)

Clients looking for legal services (professional)

Industry/Entity Type

Legal

Contact Information for Business Card

Boris Telemark
Partner
Mobile: 0438 715 642
Email: boris@kvtlaw.co
Website: www.kvtlaw.co
Level 3, 118 Wexbury Street
Sydney NSW 2000

Font styles to use
Other font styles liked:
• Avenir

Colors
f04a50
ffffff
1b1b1b

Requirements
Must have
• Black back with logo included in the centre of the card.
• Our font is Avenir.

```html
<!DOCTYPE html>
<html lang="en">
<head>
<meta charset="utf-8">
<title>KVT Legal – Business Cards</title>
<link href="https://fonts.googleapis.com/css2?family=Nunito+Sans:wght@400;600;800&display=swap" rel="stylesheet">
<style>
  :root {
    --backdrop: #e4e5e7;
    --ink: #1b1b1b;
    --crimson: #c8194b;
    --paper: #ffffff;
    --text: #2a2a2a;
    --muted: #555555;
    --pattern-dark: #1e1e1e;
    --pattern-light: #2c2c2c;
  }
  * { box-sizing: border-box; margin: 0; padding: 0; }
  html, body {
    width: 1200px; height: 800px; overflow: hidden;
    background: var(--backdrop);
    font-family: "Nunito Sans", "Avenir", sans-serif;
  }
  .sheet {
    position: relative; width: 1200px; height: 800px;
    display: flex; align-items: center; justify-content: center; gap: 60px;
  }
  .card {
    position: relative; width: 525px; height: 300px; overflow: hidden;
    box-shadow: 0 6px 18px rgba(0,0,0,0.12);
  }
  /* Front */
  .card-front { background: var(--paper); }
  .front-band { position: absolute; inset: 0; width: 100%; height: 100%; }
  .front-mark {
    position: absolute; left: 150px; top: 34px;
    width: 58px; height: 58px; background: var(--crimson);
  }
  .firm-name {
    position: absolute; left: 226px; top: 40px;
    font-weight: 800; font-size: 38px; line-height: 1; letter-spacing: 0.5px;
    color: var(--ink); text-transform: uppercase;
  }
  .contact {
    position: absolute; left: 226px; top: 128px; color: var(--text);
  }
  .person-name { font-weight: 600; font-size: 22px; color: var(--crimson); line-height: 1.1; }
  .person-role { font-size: 13px; color: var(--muted); margin-bottom: 12px; }
  .address { font-size: 14px; line-height: 1.35; margin-bottom: 4px; }
  .contact-list { list-style: none; font-size: 14px; line-height: 1.45; }
  .contact-list li { display: flex; align-items: center; gap: 6px; }
  .contact-list svg { width: 12px; height: 12px; flex: none; }
  /* Back */
  .card-back { background: var(--ink); }
  .back-pattern {
    position: absolute; inset: 0;
    background: linear-gradient(135deg, var(--pattern-light), var(--pattern-dark) 60%, var(--pattern-light));
  }
  .back-mark {
    position: absolute; left: 50%; top: 50%; transform: translate(-50%, -50%);
    display: flex; align-items: center; gap: 12px;
  }
  .back-mark .square { width: 30px; height: 30px; background: var(--crimson); }
  .back-mark .label {
    font-weight: 800; font-size: 30px; color: var(--paper);
    text-transform: uppercase; letter-spacing: 0.5px;
  }
</style>
</head>
<body>
<main class="sheet">
  <section class="card card-front" aria-label="Business card front">
    <svg class="front-band" viewBox="0 0 525 300" aria-hidden="true">
      <polygon points="0,0 140,0 68,300 0,300" fill="var(--ink)"/>
      <polygon points="140,0 146,0 74,300 68,300" fill="var(--crimson)"/>
    </svg>
    <div class="front-mark" aria-hidden="true"></div>
    <div class="firm-name">KVT Legal</div>
    <div class="contact">
      <p class="person-name">Boris Telemark</p>
      <p class="person-role">Partner</p>
      <p class="address">Level 3, 118 Wexbury Street<br>Sydney NSW 2000</p>
      <ul class="contact-list">
        <li>
          <svg viewBox="0 0 12 12" aria-hidden="true"><rect x="3" y="0.5" width="6" height="11" rx="1" fill="none" stroke="var(--crimson)" stroke-width="1.2"/><circle cx="6" cy="9.5" r="0.7" fill="var(--crimson)"/></svg>
          0438 715 642
        </li>
        <li>
          <svg viewBox="0 0 12 12" aria-hidden="true"><rect x="0.6" y="2" width="10.8" height="8" fill="none" stroke="var(--crimson)" stroke-width="1.2"/><polyline points="0.6,2 6,6.5 11.4,2" fill="none" stroke="var(--crimson)" stroke-width="1.2"/></svg>
          boris@kvtlaw.co
        </li>
        <li>
          <svg viewBox="0 0 12 12" aria-hidden="true"><circle cx="6" cy="6" r="5.3" fill="none" stroke="var(--crimson)" stroke-width="1.1"/><ellipse cx="6" cy="6" rx="2.4" ry="5.3" fill="none" stroke="var(--crimson)" stroke-width="1"/><line x1="0.7" y1="6" x2="11.3" y2="6" stroke="var(--crimson)" stroke-width="1"/></svg>
          www.kvtlaw.co
        </li>
      </ul>
    </div>
  </section>

  <section class="card card-back" aria-label="Business card back">
    <div class="back-pattern" role="img" aria-label="Subtle dark tiled pattern across the matte black back"></div>
    <div class="back-mark">
      <span class="square" aria-hidden="true"></span>
      <span class="label">KVT Legal</span>
    </div>
  </section>
</main>
</body>
</html>
```